1/2 Page add for BRMTL Conference

We are looking for a 1/2 page ad to support the annual BRMTL conference. I want to encourage the attendees to come to our both so we can explain how they can save money on food and supplies. here is a link to the conference. https://www.brmtl-example.org/conference/ here is our website www.pantrywisehub-example.com - the what we do can be captured in the ad. We will be at booth 505. Our goal is to get people to our booth #505 to explain the services that we provide –

Discounted food pricing
Free menu planning/design
Use of Registered Dietitian
Huge selection of discounted PPE and other necessary supplies to run any child care center

We have over 6000 members in 46 States and work with both small and large food distributors. We have been a sponsor of the association for the last 10 years.

Target Market(s)

Child care centers

Requirements
Must have
• Booth number -outline of what we do --- Stress we are a FREE service getting our members reduced pricing on food and supplies

```html
<!DOCTYPE html>
<html lang="en">
<head>
<meta charset="utf-8">
<title>PantryWise Hub – Booth #505</title>
<link rel="stylesheet" href="https://fonts.googleapis.com/css2?family=Orbitron:wght@900&family=Raleway:wght@400;700;800&family=Roboto:wght@700&family=Open+Sans:wght@300&family=Hind:wght@400;600&display=swap">
<style>
  :root {
    --blue: #4687c8;
    --blue-soft: #8db5df;
    --green: #9fd48f;
    --green-text: #8fcd7c;
    --ink: #111111;
    --paper: #ffffff;
    --backdrop: #8c8c8c;
  }
  * { margin: 0; padding: 0; box-sizing: border-box; }
  html, body { width: 1200px; height: 1200px; overflow: hidden; }
  body { background: var(--backdrop); position: relative; font-family: "Raleway", sans-serif; color: var(--ink); }

  .ad { position: absolute; left: 0; top: 214px; width: 1200px; height: 771px; background: var(--paper); overflow: hidden; }

  .brand { position: absolute; left: 51px; top: 66px; display: flex; align-items: center; gap: 12px; }
  .brand-mark { width: 40px; height: 40px; background: var(--blue); }
  .brand-name { font-family: "Raleway", sans-serif; font-weight: 400; font-size: 34px; color: #6b6b6b; }

  .website { position: absolute; left: 860px; top: 78px; font-family: "Hind", sans-serif; font-size: 19px; color: var(--ink); }
  .website-rule { position: absolute; left: 1151px; top: 92px; width: 49px; height: 1px; background: var(--ink); }

  .hero-photo { position: absolute; left: 746px; top: 69px; width: 454px; height: 395px;
    background:
      radial-gradient(ellipse 45% 35% at 68% 88%, rgba(130,180,70,.75), transparent 70%),
      radial-gradient(ellipse 18% 14% at 46% 80%, rgba(210,40,30,.7), transparent 70%),
      radial-gradient(ellipse 30% 40% at 65% 40%, rgba(225,190,160,.8), transparent 70%),
      radial-gradient(ellipse 25% 30% at 55% 60%, rgba(150,200,160,.7), transparent 70%),
      linear-gradient(90deg, rgba(255,255,255,1) 0%, rgba(240,242,240,.6) 25%, #eef0ee 100%); }

  .year { position: absolute; left: 51px; top: 170px; width: 624px; height: 140px; }
  .year text { font-family: "Orbitron", sans-serif; font-weight: 900; fill: var(--blue); }

  .title-divider { position: absolute; left: 721px; top: 170px; width: 1.5px; height: 244px; background: var(--ink); }

  .conference-name { position: absolute; left: 51px; top: 321px; width: 623px; height: 47px; background: var(--green);
    font-weight: 700; font-size: 32px; line-height: 47px; text-align: center; color: var(--ink); }

  .booth-line { position: absolute; left: 51px; top: 372px; display: flex; align-items: center; height: 44px; }
  .booth { font-family: "Roboto", sans-serif; font-weight: 700; font-size: 37px; color: var(--blue); }
  .booth-divider { width: 1.5px; height: 38px; background: var(--ink); margin: 0 27px 0 28px; }
  .dates { font-family: "Open Sans", sans-serif; font-weight: 300; font-size: 38px; color: var(--blue); }

  .services { position: absolute; left: 0; top: 463px; width: 1200px; height: 101px; }
  .service { position: absolute; top: 0; height: 101px; display: flex; align-items: center; gap: 16px;
    font-size: 19px; line-height: 23px; color: var(--ink); }
  .service svg { flex: none; }
  .service--green { background: linear-gradient(90deg, var(--green) 0%, var(--green) 65%, rgba(159,212,143,0) 100%); }
  .service--blue { background: linear-gradient(90deg, var(--blue-soft) 0%, var(--blue-soft) 70%, rgba(141,181,223,0) 100%); }
  .service--pricing { left: 0; width: 257px; padding-left: 50px; }
  .service--menu { left: 257px; width: 256px; padding-left: 20px; }
  .service--dietitian { left: 516px; width: 230px; padding-left: 28px; }
  .service--supplies { left: 746px; width: 520px; padding-left: 30px; }

  .section-tag { position: absolute; left: 51px; top: 590px; width: 187px; height: 37px; background: var(--blue);
    color: #fff; font-weight: 700; font-size: 21px; line-height: 37px; text-align: center; }

  .promise { position: absolute; left: 51px; top: 632px; width: 360px; font-size: 21px; line-height: 25px; }
  .promise strong { color: var(--green-text); font-weight: 800; font-size: 24px; margin-left: 6px; }

  .about { position: absolute; left: 479px; top: 650px; width: 682px; font-family: "Hind", sans-serif;
    font-size: 18px; line-height: 23px; text-align: justify; text-align-last: left; }

  .conference-link { position: absolute; left: 477px; top: 697px; font-family: "Hind", sans-serif; font-size: 18px; }
  .conference-link b { font-weight: 600; margin-right: 20px; }
  .conference-link a { color: var(--blue); font-weight: 600; text-decoration: none; }

  .footer-band { position: absolute; left: 0; bottom: 0; width: 1200px; height: 34px; background: var(--blue); }
</style>
</head>
<body>
  <main class="ad">
    <div class="brand">
      <span class="brand-mark"></span>
      <span class="brand-name">PantryWise Hub</span>
    </div>

    <div class="website">www.pantrywisehub-example.com</div>
    <div class="website-rule"></div>

    <div class="hero-photo" role="img" aria-label="Photo of a young girl playfully holding red bell pepper rings over her eyes beside a bowl of fresh salad vegetables"></div>

    <svg class="year" viewBox="0 0 624 140" aria-label="2022">
      <text x="0" y="138" font-size="190" textLength="624" lengthAdjust="spacingAndGlyphs">2022</text>
    </svg>

    <div class="title-divider"></div>

    <h1 class="conference-name">National Child Nutrition Conference</h1>

    <div class="booth-line">
      <span class="booth">Our Booth #505</span>
      <span class="booth-divider"></span>
      <span class="dates">April 18-22, 2022</span>
    </div>

    <section class="services">
      <div class="service service--green service--pricing">
        <svg width="50" height="50" viewBox="0 0 50 50" aria-hidden="true">
          <polygon fill="#111" points="25,1 30,6 37,4 39,11 46,13 44,20 49,25 44,30 46,37 39,39 37,46 30,44 25,49 20,44 13,46 11,39 4,37 6,30 1,25 6,20 4,13 11,11 13,4 20,6"/>
          <circle cx="18" cy="18" r="4.5" fill="none" stroke="#fff" stroke-width="3"/>
          <circle cx="32" cy="32" r="4.5" fill="none" stroke="#fff" stroke-width="3"/>
          <line x1="33" y1="15" x2="17" y2="35" stroke="#fff" stroke-width="3"/>
        </svg>
        <span>Discounted<br>food pricing</span>
      </div>
      <div class="service service--blue service--menu">
        <svg width="48" height="50" viewBox="0 0 48 50" aria-hidden="true">
          <circle cx="24" cy="6" r="3" fill="#2e4257"/>
          <path d="M4 28 A20 20 0 0 1 44 28 Z" fill="#2e4257"/>
          <rect x="1" y="30" width="46" height="4" rx="2" fill="#2e4257"/>
          <path d="M6 48 L12 40 Q18 36 26 38 L36 38 Q40 38 38 42 L28 44" fill="none" stroke="#2e4257" stroke-width="4" stroke-linecap="round"/>
        </svg>
        <span>Free menu<br>planning/design</span>
      </div>
      <div class="service service--green service--dietitian">
        <svg width="52" height="50" viewBox="0 0 52 50" aria-hidden="true">
          <circle cx="22" cy="13" r="10" fill="none" stroke="#222" stroke-width="2"/>
          <path d="M2 42 Q2 28 22 28 Q34 28 38 34 M2 42 L30 42" fill="none" stroke="#222" stroke-width="2"/>
          <path d="M34 40 L40 46 L50 34" fill="none" stroke="#222" stroke-width="2"/>
        </svg>
        <span>Use of<br>Registered<br>Dietitian</span>
      </div>
      <div class="service service--blue service--supplies">
        <svg width="46" height="50" viewBox="0 0 46 50" aria-hidden="true" fill="none" stroke="#3b3a7a" stroke-width="2">
          <circle cx="6" cy="6" r="4"/><line x1="2" y1="6" x2="10" y2="6"/>
          <rect x="1" y="14" width="10" height="34" rx="2"/><line x1="3" y1="24" x2="9" y2="24"/><line x1="3" y1="30" x2="9" y2="30"/><line x1="3" y1="36" x2="9" y2="36"/>
          <rect x="16" y="2" width="10" height="6"/><path d="M17 8 L17 44 Q21 50 25 44 L25 8"/>
          <rect x="30" y="12" width="8" height="36"/><line x1="34" y1="2" x2="34" y2="12"/><line x1="30" y1="22" x2="34" y2="22"/><line x1="30" y1="30" x2="34" y2="30"/>
          <line x1="42" y1="20" x2="42" y2="48"/><line x1="38" y1="48" x2="45" y2="48"/>
        </svg>
        <span>Huge selection of discounted<br>PPE and other necessary supplies<br>to run any child care center</span>
      </div>
    </section>

    <h2 class="section-tag">WHAT WE DO</h2>
    <p class="promise">Stress we are a <strong>FREE SERVICE</strong><br>getting our members reduced<br>pricing on food and supplies</p>

    <p class="about">We have over 6000 members in 46 States and work with both small and large food distributors. We have been a sponsor of the association for the last 10 years.</p>

    <p class="conference-link"><b>Here is a link to the conference</b><a href="https://www.brmtl-example.org/conference/">https://www.brmtl-example.org/conference/</a></p>

    <div class="footer-band"></div>
  </main>
</body>
</html>
```